Haunted Attraction Expert Website Design

A complete professional looking web site with 6 total pages.
Includes calendar and email form.
Needs to be word press and mobile user friendly.
Please use photos as labeled for the pages they will be presented on.
Company logo should alternate left and right sides of the page.
See attached layout for directions

Target Market(s)

Professionals, Haunted Attraction Owners/Operators

Industry/Entity Type

It Professional

Coding

Coded - Design and coding required

Number of Pages Required

5+ page

Font styles to use
Sans Serif

Colors

Designer to choose colors to be used in the design.

Requirements
Must have
• Our company logo on each page and photos supplied by me assigned to specific pages.
• Calendar
• Contact US Email Submission Form

```html
<!DOCTYPE html>
<html lang="en">
<head>
<meta charset="utf-8">
<title>Nightfall Venue Advisors — Expert Witnesses</title>
<link rel="stylesheet" href="https://fonts.googleapis.com/css2?family=Montserrat:ital,wght@0,300;0,400;0,600;0,700;1,300&display=swap">
<style>
  :root {
    --forest: #133a06;
    --nav-grey: #a4a5a7;
    --orange: #e8861a;
    --white: #ffffff;
    --button-grey: #a9aaac;
    --button-text: #133a06;
    --footer: #1b2410;
    --footer-text: #b9bcb3;
    --photo-dark: #2a2422;
    --photo-mid: #5b4a40;
    --photo-warm: #7a5a48;
  }
  * { margin: 0; padding: 0; box-sizing: border-box; }
  html, body { width: 872px; height: 1200px; overflow: hidden; }
  body {
    position: relative;
    background: var(--forest);
    font-family: "Montserrat", sans-serif;
    font-weight: 300;
    color: var(--white);
  }
  .brand {
    position: absolute; left: 107px; top: 30px;
    color: var(--orange); font-weight: 600; font-size: 17px;
    line-height: 1.15; width: 130px;
  }
  .main-nav {
    position: absolute; left: 0; top: 100px; width: 872px; height: 55px;
    background: var(--nav-grey);
  }
  .main-nav a {
    position: absolute; top: 19px; font-size: 13px; font-weight: 400;
    color: var(--white); text-decoration: none; white-space: nowrap;
  }
  .main-nav a.current { font-weight: 700; }
  .intro {
    position: absolute; left: 107px; top: 225px; width: 670px;
    font-size: 14.6px; line-height: 16.8px;
  }
  .intro p + p { margin-top: 16px; }
  .intro .company { color: var(--orange); }
  .expert {
    position: absolute; left: 107px; width: 640px;
    font-size: 14.6px; line-height: 16.8px;
  }
  .expert .name { color: var(--orange); }
  .cv-button {
    position: absolute; left: 427px; top: 5px; width: 79px; height: 20px;
    background: var(--button-grey); color: var(--button-text);
    font-size: 12px; font-weight: 700; text-align: center; line-height: 20px;
  }
  .feature-photo {
    position: absolute; left: 108px; top: 597px; width: 662px; height: 330px;
    background: linear-gradient(100deg, var(--photo-mid) 0%, var(--photo-dark) 45%, var(--photo-warm) 75%, var(--photo-dark) 100%);
  }
  .quote-mark {
    position: absolute; left: 132px; top: 982px;
    font-family: "Georgia", serif; font-weight: 700; font-size: 86px; line-height: 1;
  }
  .quote {
    position: absolute; left: 203px; top: 1016px; width: 560px;
  }
  .quote blockquote { font-size: 21px; font-weight: 600; line-height: 20px; }
  .quote cite { display: block; margin-top: 16px; font-size: 14px; font-style: italic; }
  .site-footer {
    position: absolute; left: 0; top: 1172px; width: 872px; height: 28px;
    background: var(--footer); color: var(--footer-text);
    font-size: 10.5px; font-weight: 400; line-height: 28px;
  }
  .site-footer span { position: absolute; }
</style>
</head>
<body>
  <div class="brand">Nightfall Venue Advisors</div>

  <nav class="main-nav">
    <a style="left:104px">Home</a>
    <a style="left:190px">About</a>
    <a style="left:277px">Consulting</a>
    <a class="current" style="left:391px">Expert Witnesses</a>
    <a style="left:552px">Upcoming events</a>
    <a style="left:707px">Contact Us</a>
  </nav>

  <section class="intro">
    <p><span class="company">Nightfall Venue Advisors NVA</span> provide forensic litigation consulting and expert witness services for lawsuits and legal cases involving catastrophic injuries, fatalities, personal injuries, and workplace safety.</p>
    <p>To discuss litigation consulting or expert witness services contact one of our Industry Experts below:</p>
  </section>

  <div class="expert" style="top:341px">
    <div class="name">Daniel Whitmore</div>
    <div>Email: dwhitmore@nightfallmail.com, Phone: 555-201-4837</div>
    <div class="cv-button">Read CV</div>
  </div>
  <div class="expert" style="top:391px">
    <div class="name">Marcus Ellery</div>
    <div>Email marcus@hollowlanetours.com, Phone: 555-348-1920</div>
    <div class="cv-button">Read CV</div>
  </div>
  <div class="expert" style="top:441px">
    <div class="name">Owen Castellan</div>
    <div>Email ocastellan@mailbox.net, Phone: 555-672-0415</div>
    <div class="cv-button">Read CV</div>
  </div>
  <div class="expert" style="top:491px">
    <div class="name">Peter Vantassel</div>
    <div>Email peter@fogworks.com, Phone: 555-903-2286</div>
    <div class="cv-button">Read CV</div>
  </div>

  <div class="feature-photo" role="img" aria-label="Costumed haunted attraction performer in a hat reading a letter beside an antique typewriter in a dim, cluttered set"></div>

  <div class="quote-mark">“</div>
  <figure class="quote">
    <blockquote>Happiness and personal fulfillment are the natural consequences of doing the right thing.</blockquote>
    <cite>Aurelian Voss</cite>
  </figure>

  <footer class="site-footer">
    <span style="left:246px">© 2018 Nightfall Venue Advisors</span>
    <span style="left:452px">Privacy Policy</span>
    <span style="left:550px">Terms of Service</span>
  </footer>
</body>
</html>
```